USA Chronic pain vitamin needs a label design for bottle

It needs to look modern and clean. No tacky color or cheap looking font. Prefer experienced designers with experience in creating labels for healthcare products. The color schemes are attached. The logo is also attached. Please keep the Soltera Bloom and the logo either Lime Green or Yellow. You can mix in a light gray and white as accent colors. You can add your own touch to it, doesn't need to look exactly how I did it. We are a nerve supplement company that helps people manage their chronic pain and diabetic neuropathy naturally. Colors very similar to Quenzo.

I want an area underneath the large N that breaks it down for the client
+ Relieves Acute & Chronic Pain
+ Reduces Inflammation
+ Supports Optimal Nerve Health
+ Immunity Booster

```html
<!DOCTYPE html>
<html lang="en">
<head>
<meta charset="UTF-8">
<title>Soltera Bloom – Label</title>
<link href="https://fonts.googleapis.com/css2?family=Montserrat:wght@500;600;800&display=swap" rel="stylesheet">
<style>
  :root {
    --bg: #ececec;
    --white: #ffffff;
    --green: #3aa95a;
    --green-deep: #2f9a4c;
    --yellow: #f6b90f;
    --ink-white: #ffffff;
  }
  html, body {
    margin: 0;
    padding: 0;
    width: 1200px;
    height: 1200px;
    overflow: hidden;
    background: var(--bg);
    font-family: "Montserrat", Arial, sans-serif;
  }
  .canvas {
    position: relative;
    width: 1200px;
    height: 1200px;
  }
  .label {
    position: absolute;
    left: 130px;
    top: 75px;
    width: 940px;
    height: 1050px;
    background: var(--white);
    box-shadow: 0 8px 30px rgba(0,0,0,0.08);
  }
  .brand-strip {
    position: absolute;
    left: 0;
    top: 0;
    width: 268px;
    height: 100%;
    display: flex;
    align-items: center;
    justify-content: center;
  }
  .brand-vertical {
    writing-mode: vertical-rl;
    transform: rotate(180deg);
    font-weight: 800;
    font-size: 98px;
    letter-spacing: 2px;
    line-height: 1;
    white-space: nowrap;
    text-transform: uppercase;
  }
  .brand-vertical .word-one { color: var(--yellow); }
  .brand-vertical .word-two { color: var(--green); }

  .info-panel {
    position: absolute;
    left: 268px;
    top: 0;
    right: 0;
    bottom: 0;
    background: linear-gradient(135deg, var(--green-deep), var(--green));
    border-top-left-radius: 46px;
    color: var(--ink-white);
  }
  .panel-pointer {
    position: absolute;
    left: 268px;
    top: 725px;
    width: 60px;
    height: 76px;
  }
  .meta-row {
    position: absolute;
    top: 80px;
    left: 60px;
    right: 60px;
    display: flex;
    justify-content: space-between;
    align-items: center;
    font-weight: 600;
    font-size: 30px;
  }
  .meta-item {
    display: flex;
    align-items: center;
    gap: 18px;
  }
  .flag-chip {
    width: 66px;
    height: 38px;
    background: var(--yellow);
    border-radius: 3px;
  }
  .count-badge {
    width: 54px;
    height: 54px;
    border-radius: 50%;
    background: var(--yellow);
    color: var(--white);
    font-weight: 800;
    font-size: 24px;
    display: flex;
    align-items: center;
    justify-content: center;
  }
  .brand-mark {
    position: absolute;
    top: 250px;
    left: 0;
    right: 0;
    display: flex;
    align-items: center;
    justify-content: center;
    gap: 34px;
  }
  .brand-mark-square {
    width: 92px;
    height: 92px;
    background: var(--white);
    flex: none;
  }
  .brand-mark-name {
    color: var(--yellow);
    font-weight: 800;
    font-size: 84px;
    line-height: 1.02;
  }
  .benefits {
    position: absolute;
    left: 74px;
    top: 805px;
    margin: 0;
    padding: 0;
    list-style: none;
    font-weight: 500;
    font-size: 30px;
    line-height: 1;
  }
  .benefits li {
    display: flex;
    align-items: center;
    gap: 20px;
    margin-bottom: 27px;
  }
  .benefit-plus {
    width: 22px;
    height: 22px;
    flex: none;
  }
</style>
</head>
<body>
<div class="canvas">
  <section class="label">
    <div class="brand-strip">
      <div class="brand-vertical"><span class="word-one">Soltera</span> <span class="word-two">Bloom</span></div>
    </div>

    <div class="info-panel">
      <div class="meta-row">
        <div class="meta-item"><span class="flag-chip"></span>Made In USA</div>
        <div class="meta-item"><span class="count-badge">60</span>Capsules</div>
      </div>

      <div class="brand-mark">
        <span class="brand-mark-square"></span>
        <span class="brand-mark-name">Soltera<br>Bloom</span>
      </div>

      <ul class="benefits">
        <li><svg class="benefit-plus" viewBox="0 0 22 22"><path d="M8 0h6v8h8v6h-8v8H8v-8H0V8h8z" fill="#f6b90f"/></svg>Relieves Acute &amp; Chronic Pain</li>
        <li><svg class="benefit-plus" viewBox="0 0 22 22"><path d="M8 0h6v8h8v6h-8v8H8v-8H0V8h8z" fill="#f6b90f"/></svg>Reduces Inflammation</li>
        <li><svg class="benefit-plus" viewBox="0 0 22 22"><path d="M8 0h6v8h8v6h-8v8H8v-8H0V8h8z" fill="#f6b90f"/></svg>Supports Optimal Nerve Health</li>
        <li><svg class="benefit-plus" viewBox="0 0 22 22"><path d="M8 0h6v8h8v6h-8v8H8v-8H0V8h8z" fill="#f6b90f"/></svg>Immunity Booster</li>
      </ul>
    </div>

    <svg class="panel-pointer" viewBox="0 0 60 76"><path d="M0 0 L44 38 L0 76 Z" fill="#ffffff"/></svg>
  </section>
</div>
</body>
</html>
```